Rivex Management LLC Business Card

The sample logo was attached for the business Card Design for Traffic Control Company named Rivex Management LLC. Card design needs to have the company logo and colors match the logo color. It will be nice to show some images of Traffic control signs or cones, even roads closer that math the company services

Target Market(s)

Temporary traffic control. Road closer.

Industry/Entity Type

Construction

Contact Information for Business Card

basic information, name, job title, address, email phone, website

Font styles to use
Serif
Sans Serif

Colors
F0912C
F2A743
F7CA91
FBE8D2
FDF5EE
EE7325
F08F49
F5BC92
FAE3D3
FDF4ED

```html
<!DOCTYPE html>
<html lang="en">
<head>
<meta charset="utf-8">
<title>Rivex Management LLC – Business Card</title>
<link href="https://fonts.googleapis.com/css2?family=Montserrat:wght@600&family=Arimo:wght@400&display=swap" rel="stylesheet">
<style>
  :root {
    --orange: #EE7325;
    --charcoal: #3A3A3A;
    --grey-line: #8A8A8A;
    --paper: #FFFFFF;
    --backdrop: #2B2B2B;
  }
  * { box-sizing: border-box; margin: 0; padding: 0; }
  html, body { width: 1200px; height: 1108px; overflow: hidden; }
  body {
    background: var(--backdrop);
    position: relative;
    font-family: "Arimo", Arial, sans-serif;
  }
  .card {
    position: absolute;
    top: 194px;
    width: 420px;
    height: 720px;
    border-radius: 30px;
    overflow: hidden;
  }
  .card-front { left: 150px; background: var(--paper); }
  .card-back { left: 630px; background: var(--orange); }

  .company {
    position: absolute; left: 0; width: 100%;
    display: flex; align-items: center; justify-content: center; gap: 12px;
    font-family: "Arimo", Arial, sans-serif;
    font-weight: 400;
    white-space: nowrap;
  }
  .company .mark { width: 18px; height: 18px; }
  .front-company { top: 150px; font-size: 30px; color: var(--charcoal); }
  .front-company .mark { background: var(--orange); }
  .back-company { top: 575px; font-size: 26px; color: var(--paper); }
  .back-company .mark { background: var(--paper); }

  .holder {
    position: absolute; top: 318px; width: 100%; text-align: center;
  }
  .holder-name {
    font-family: "Montserrat", Arial, sans-serif;
    font-weight: 600; font-size: 31px; color: var(--orange); letter-spacing: 0.5px;
  }
  .holder-role {
    font-size: 24px; color: var(--charcoal); margin-top: 2px;
  }
  .icon-row {
    position: absolute; top: 424px; left: 40px; right: 40px;
    display: flex; align-items: center; gap: 12px;
  }
  .icon-row .rule { flex: 1; height: 1px; background: var(--grey-line); }
  .icon-badge {
    width: 38px; height: 38px; border-radius: 8px; background: var(--orange);
    display: flex; align-items: center; justify-content: center;
  }
  .icon-badge svg { width: 24px; height: 24px; }
  .contact-list {
    position: absolute; top: 484px; width: 100%; text-align: center;
    list-style: none; font-size: 25px; line-height: 34px; color: var(--charcoal);
  }
  .divider {
    position: absolute; top: 600px; left: 50px; right: 50px;
    height: 1px; background: var(--grey-line);
  }
  .address {
    position: absolute; top: 616px; width: 100%; text-align: center;
    font-size: 25px; line-height: 32px; color: var(--charcoal);
  }

  .back-pattern {
    position: absolute; inset: 0;
    background: linear-gradient(135deg, var(--orange) 0%, #E86E22 50%, var(--orange) 100%);
  }
</style>
</head>
<body>
  <section class="card card-front">
    <div class="company front-company"><span class="mark"></span>Rivex Management LLC</div>

    <div class="holder">
      <div class="holder-name">DANIEL BROOKS</div>
      <div class="holder-role">Manager</div>
    </div>

    <div class="icon-row">
      <span class="rule"></span>
      <span class="icon-badge" aria-label="phone">
        <svg viewBox="0 0 24 24"><path fill="#fff" d="M6.6 10.8a15 15 0 0 0 6.6 6.6l2.2-2.2c.3-.3.7-.4 1-.2 1.1.4 2.3.6 3.6.6.6 0 1 .4 1 1V20c0 .6-.4 1-1 1A17 17 0 0 1 3 4c0-.6.4-1 1-1h3.5c.6 0 1 .4 1 1 0 1.3.2 2.5.6 3.6.1.3 0 .7-.2 1z"/></svg>
      </span>
      <span class="icon-badge" aria-label="email">
        <svg viewBox="0 0 24 24"><rect x="3" y="6" width="18" height="12" rx="1.5" fill="none" stroke="#fff" stroke-width="2"/><path d="M3.5 7l8.5 6.5L20.5 7" fill="none" stroke="#fff" stroke-width="2"/></svg>
      </span>
      <span class="icon-badge" aria-label="website">
        <svg viewBox="0 0 24 24" fill="none" stroke="#fff" stroke-width="1.8"><circle cx="12" cy="12" r="8.5"/><ellipse cx="12" cy="12" rx="3.8" ry="8.5"/><path d="M3.5 12h17"/></svg>
      </span>
      <span class="rule"></span>
    </div>

    <ul class="contact-list">
      <li>123-456-2100</li>
      <li>youremail@mailbox.com</li>
      <li>www.yourwebsite.com</li>
    </ul>

    <div class="divider"></div>

    <p class="address">Your address, city<br>state, ZIP 0000</p>
  </section>

  <section class="card card-back">
    <div class="back-pattern" role="img" aria-label="Tone-on-tone embossed repeating pattern in deeper orange"></div>
    <div class="company back-company"><span class="mark"></span>Rivex Management LLC</div>
  </section>
</body>
</html>
```